Flyer-Design für Lumira Afghan Take Away
Zielgruppe
Gastrobetrieb mit Afghanischer Küche. Hauptangebot: Reisgerichte, Teigtaschen und Korma (Currygerichte). ZG: Studenten/Schüller, Ladenbesitzer und Passanten, da es sehr Zentral liegt
Aufgabenstellung
Öffnungszeiten:
MO: 11:30-14h
DI&MI: 11:30-14h/18h-20h
DO&FR: 11:30-14h/18h-21h
SA: 11:30-15h
SO: Geschlossen
INFO: www.lumira-imbiss.ch

```html
<!DOCTYPE html>
<html lang="de">
<head>
<meta charset="utf-8">
<title>Lumira Afghan Take Away – Flyer</title>
<link href="https://fonts.googleapis.com/css2?family=Montserrat:ital,wght@0,400;0,500;0,600;0,700;0,800;1,700&display=swap" rel="stylesheet">
<style>
  :root{
    --maroon:#8a2626;
    --red:#c8102e;
    --blob:#d71920;
    --ink:#1d1d1d;
    --green:#2e6b2a;
    --paper-1:#f2f2f2;
    --paper-2:#d9d9d9;
    --card-1:#fbf3ea;
    --card-2:#e8d6c2;
    --stage:#eeeeee;
  }
  *{box-sizing:border-box;margin:0;padding:0}
  html,body{width:1200px;height:1200px;overflow:hidden}
  body{background:var(--stage);font-family:'Montserrat',sans-serif;color:var(--ink);position:relative}

  .flyer{position:absolute;top:98px;width:510px;height:1003px;overflow:hidden;background:#fff;box-shadow:0 2px 10px rgba(0,0,0,.12)}
  .flyer--menu{left:80px;background:var(--maroon)}
  .flyer--specials{left:610px}

  .paper{position:absolute;left:0;top:0;width:510px;height:893px}

  /* menu list */
  .menu{position:absolute;left:82px;top:78px;width:334px}
  .menu__heading{font-weight:800;color:var(--red);font-size:14.5px;letter-spacing:.2px;display:flex;justify-content:space-between;align-items:baseline;margin-bottom:4px}
  .menu__heading small{font-size:7px;color:#555;font-weight:600}
  .menu__heading--daily{margin-top:34px}
  .dish{display:grid;grid-template-columns:42px 1fr auto;column-gap:4px;border-bottom:1px solid var(--red);padding:3px 0 2px}
  .dish__day{font-weight:800;color:var(--red);font-size:15px;line-height:18px}
  .dish__name{font-weight:700;font-size:14.5px;line-height:18px;grid-column:2}
  .dish__desc{font-size:8.3px;line-height:10.6px;color:#333;grid-column:2}
  .dish__price{grid-column:3;grid-row:1 / span 3;align-self:end;font-weight:600;font-size:16px;line-height:18px}
  .dish--daily{grid-template-columns:1fr auto}
  .dish--daily .dish__name,.dish--daily .dish__desc{grid-column:1}
  .dish--daily .dish__price{grid-column:2}
  .menu__note{text-align:right;font-size:8px;color:var(--red);margin-top:44px}

  /* footer */
  .footer{position:absolute;left:0;bottom:0;width:510px;height:110px;background:var(--maroon);color:#fff;display:flex;align-items:center}
  .brand{width:150px;text-align:center;font-weight:800;line-height:1.05}
  .brand--footer{color:#fff;font-size:17px;padding-left:16px}
  .footer__divider{height:80px;border-left:3px dotted #fff;margin:0 18px 0 20px}
  .address{display:flex;align-items:center;gap:10px}
  .address__text{font-weight:700;font-size:20px;line-height:1.1}
  .address__text span{display:block;font-size:17px}

  /* special cards */
  .card{position:absolute;left:9px;width:370px;height:205px;border-radius:4px;background:linear-gradient(180deg,#fff 0%,var(--card-1) 35%,var(--card-2) 100%);padding:10px 14px}
  .card__title{color:var(--red);font-weight:700;font-size:15px;line-height:18px}
  .card__desc{color:var(--red);font-size:9.5px;line-height:12px;width:300px}
  .card__photo{position:absolute;left:85px;bottom:14px;width:200px;height:118px;border-radius:50%;background:radial-gradient(ellipse at center,#ffffff 0%,#f1e6da 55%,rgba(232,214,194,0) 72%)}
  .card__price{position:absolute;right:18px;bottom:14px;width:66px;height:66px;border-radius:50%;background:var(--blob);color:#fff;font-weight:700;font-style:italic;font-size:21px;display:flex;align-items:center;justify-content:center}

  .brand--top{position:absolute;left:383px;top:90px;width:110px;color:var(--maroon);font-size:17px}

  .hours{position:absolute;left:388px;top:868px;width:510px;transform:rotate(-90deg);transform-origin:top left;font-weight:700;font-size:14.5px;line-height:17px;color:var(--ink)}
  .hours__web{color:var(--green)}
</style>
</head>
<body>

<section class="flyer flyer--menu">
  <svg class="paper" viewBox="0 0 510 893" aria-hidden="true">
    <defs>
      <linearGradient id="paperTone" x1="0" y1="0" x2="1" y2="1">
        <stop offset="0" stop-color="#f4f4f4"/>
        <stop offset=".5" stop-color="#dedede"/>
        <stop offset="1" stop-color="#ededed"/>
      </linearGradient>
    </defs>
    <path d="M0,72 C120,48 260,40 400,0 L510,0 L510,893 L0,893 Z" fill="url(#paperTone)"/>
  </svg>

  <div class="menu">
    <h2 class="menu__heading">HAUSGEMACHTE MITTAGSMENÜ: <small>CHF</small></h2>

    <div class="dish"><span class="dish__day">MO:</span><span class="dish__name">Lawang</span><span class="dish__desc">Pouletbrustgeschn. in Kurkuma-Joghurt-Sauce und frischen Kräuter, dazu Brechbohnen Qorma und Basmatireis</span><span class="dish__price">14.50</span></div>
    <div class="dish"><span class="dish__day">DI:</span><span class="dish__name">Qorma Tschalau</span><span class="dish__desc">Basmatireis mit würzigem Rindfleisch, dazu Sabzi (gebratener Spinat)</span><span class="dish__price">14.50</span></div>
    <div class="dish"><span class="dish__day">MI:</span><span class="dish__name">Kofta Tschalau</span><span class="dish__desc">Basmatireis mit Kofta (Afgh. Meatballs), Dal (Linsen)</span><span class="dish__price">14.50</span></div>
    <div class="dish"><span class="dish__day">DO:</span><span class="dish__name">Kabuli-Palau mit Pouletfleisch</span><span class="dish__desc">Brauner Basmatireis mit Karottenstreifen, Rosinen, gekochtem Pouletfleisch und Qorme-e Gulpi (Blumenkohl an Tomatensauce)</span><span class="dish__price">14.50</span></div>
    <div class="dish"><span class="dish__day"></span><span class="dish__name">Kabuli-Palau mit Lamm-Qorma</span><span class="dish__desc">Brauner Basmati-Reis mit Karottenstr., Rosinen, Lamm-Qorma und Qorme-e Gulpi (Blumenkohl an Tomaten.)</span><span class="dish__price">16.50</span></div>
    <div class="dish"><span class="dish__day">FR:</span><span class="dish__name">Mahi Tschalau</span><span class="dish__desc">Basmatireis mit Fisch-Qourma und Qorme-e Sabzi (gebratener Spinat mit Bohnen)</span><span class="dish__price">14.50</span></div>
    <div class="dish"><span class="dish__day"></span><span class="dish__name">Lawang</span><span class="dish__desc">Pouletgeschn. in Kurkuma-Joghurt-Sauce und fr. Kräuter, Qorme-e Sabzi (gebr. Spinat mit Bohnen), Basmatireis</span><span class="dish__price">14.50</span></div>
    <div class="dish"><span class="dish__day">SA:</span><span class="dish__name">Kabuli-Palau mit Pouletfleisch</span><span class="dish__desc">Brauner Basmatireis mit Karottenstreifen, Rosinen, gekochtem Pouletfleisch und Qorme-e Gulpi (Blumenkohl an Tomatensauce)</span><span class="dish__price">14.50</span></div>
    <div class="dish"><span class="dish__day"></span><span class="dish__name">Kabuli-Palau mit Lamm-Qorma</span><span class="dish__desc">Brauner Basmati-Reis mit Karottenstreifen, Rosinen, Lamm-Qorma und Qorme-e Gulpi (Blumenkohl an Tomatensauce)</span><span class="dish__price">16.50</span></div>

    <h2 class="menu__heading menu__heading--daily">TÄGLICHES ANGEBOT:</h2>

    <div class="dish dish--daily"><span class="dish__name">Mantu</span><span class="dish__desc">Gedämpfte Rindhackfleischtaschen aus frischem Teig, dazu Tomatensauce mit gelben Erbsen und Joghurt-Minze-Sauce</span><span class="dish__price">14.00</span></div>
    <div class="dish dish--daily"><span class="dish__name">Ashak</span><span class="dish__desc">Gedämpfte Lauchtaschen aus frischem Teig, dazu Tomatensauce mit gelben Erbsen und Joghurt-Minze-Sauce</span><span class="dish__price">14.00</span></div>
    <div class="dish dish--daily"><span class="dish__name">Chapli-Kabob im Taschenbrot</span><span class="dish__desc">Gebratene Rindshacksteaks mit Gemüse, Salat, Chili-Koriander und Joghurt-Minze-Sauce</span><span class="dish__price">9.00</span></div>
    <div class="dish dish--daily"><span class="dish__name">2 Stk. Sambosa</span><span class="dish__desc">Frittierte Kartoffel oder Gemüsetaschen, dazu Chili-Koriandersauce und Joghurt-Minze-Sauce</span><span class="dish__price">6.00</span></div>
    <div class="dish dish--daily"><span class="dish__name">Unsere Empfehlung: Lumira-Teller</span><span class="dish__desc">Mix aus Tages-Menü und Teigtaschen</span><span class="dish__price">19.50</span></div>

    <p class="menu__note">Wir haben auch Studenten-Rabatt!</p>
  </div>

  <footer class="footer">
    <div class="brand brand--footer">LUMIRA<br>AFGHAN<br>TAKE AWAY</div>
    <div class="footer__divider"></div>
    <div class="address">
      <svg width="20" height="28" viewBox="0 0 20 28" aria-hidden="true"><path d="M10 0C4.5 0 0 4.4 0 9.9 0 17.3 10 28 10 28s10-10.7 10-18.1C20 4.4 15.5 0 10 0zm0 14a4.2 4.2 0 1 1 0-8.4 4.2 4.2 0 0 1 0 8.4z" fill="#fff"/></svg>
      <p class="address__text">Lindenhofgasse 7<span>8001 Zürich</span></p>
    </div>
  </footer>
</section>

<section class="flyer flyer--specials">
  <article class="card" style="top:9px">
    <h3 class="card__title">Mantu</h3>
    <p class="card__desc">Gedämpfte Rindhackfleischtaschen aus frischem Teig, dazu Tomatensauce mit gelben Erbsen und Joghurt-Minze-Sauce</p>
    <div class="card__photo" role="img" aria-label="Foto: Teller mit Mantu, Tomatensauce und Joghurt"></div>
    <div class="card__price">14.-</div>
  </article>
  <article class="card" style="top:227px">
    <h3 class="card__title">Ashak</h3>
    <p class="card__desc">Gedämpfte Lauchtaschen aus frischem Teig, dazu Tomatensauce mit gelben Erbsen und Joghurt-Minze-Sauce</p>
    <div class="card__photo" role="img" aria-label="Foto: Teller mit Ashak und Joghurt-Minze-Sauce"></div>
    <div class="card__price">14.-</div>
  </article>
  <article class="card" style="top:445px">
    <h3 class="card__title">Chapli-Kabob im Taschenbrot</h3>
    <p class="card__desc">Gebratene Rindshacksteaks mit Gemüse, Salat, Chili-Koriander und Joghurt-Minze-Sauce</p>
    <div class="card__photo" role="img" aria-label="Foto: Chapli-Kabob im Taschenbrot mit Salat"></div>
    <div class="card__price">9.-</div>
  </article>
  <article class="card" style="top:660px">
    <h3 class="card__title">Sambosa <span style="font-weight:500">2 Stk.</span></h3>
    <p class="card__desc">Frittierte Kartoffel oder Gemüsetaschen, dazu Chili-Koriandersauce und Joghurt-Minze-Sauce</p>
    <div class="card__photo" role="img" aria-label="Foto: zwei Sambosa mit zwei Saucen"></div>
    <div class="card__price">6.-</div>
  </article>

  <div class="brand brand--top">LUMIRA<br>AFGHAN<br>TAKE AWAY</div>

  <div class="hours">
    <p>Öffnungszeiten:</p>
    <p>MO: 11:30-14h &nbsp;- &nbsp;&nbsp;DI&amp;MI: 11:30-14h/18h-20h</p>
    <p>DO&amp;FR: 11:30-14h/18h-21h</p>
    <p>SA: 11:30-15h &nbsp;&nbsp;- &nbsp;&nbsp;SO: Geschlossen</p>
    <p class="hours__web">www.lumira-imbiss.ch</p>
  </div>

  <footer class="footer">
    <div class="brand brand--footer">LUMIRA<br>AFGHAN<br>TAKE AWAY</div>
    <div class="footer__divider"></div>
    <div class="address">
      <svg width="20" height="28" viewBox="0 0 20 28" aria-hidden="true"><path d="M10 0C4.5 0 0 4.4 0 9.9 0 17.3 10 28 10 28s10-10.7 10-18.1C20 4.4 15.5 0 10 0zm0 14a4.2 4.2 0 1 1 0-8.4 4.2 4.2 0 0 1 0 8.4z" fill="#fff"/></svg>
      <p class="address__text">Lindenhofgasse 7<span>8001 Zürich</span></p>
    </div>
  </footer>
</section>

</body>
</html>
```